Peter Lasko-Wren Finance

Need a personal website advertising Equipment Finance,Business Finance,Commercial Finance, Construction Finance, Bridging Finance. Similar websites are www.varoplend.com.au / www.kitmoxa.com.au / www.rzb4.com.au /wwwbelvaxcredit.com.au

Target Market(s)

Business People

Industry/Entity Type

Business

Number of Pages Required

3 page

Font styles to use
Serif
Sans Serif

Requirements
Must have
• All i want is a simple corporate looking website advertising Equipment Finance, Commercial Finance, Construction Finance, Business Finance, Bridging Finance,

```html
<!DOCTYPE html>
<html lang="en">
<head>
<meta charset="utf-8">
<title>Peter Lasko-Wren Finance</title>
<link rel="stylesheet" href="https://fonts.googleapis.com/css2?family=Tinos:ital,wght@0,400;0,700;1,400&family=Open+Sans:ital,wght@0,400;0,600;1,400&family=Raleway:wght@400;500;600&display=swap">
<style>
:root{
  --navy:#1b4d86;
  --navy-dark:#123a69;
  --blue:#1c68b5;
  --sky:#2a8fd4;
  --ink:#222;
  --muted:#555;
  --grey-bar:#e6e7e8;
  --footer:#0d4f94;
  --dark:#2e2e2e;
  --white:#fff;
}
*{box-sizing:border-box;margin:0;padding:0}
html,body{width:1200px;height:2594px;overflow:hidden;background:var(--white)}
body{position:relative;font-family:"Open Sans",Arial,sans-serif;color:var(--ink)}
.abs{position:absolute}
.serif{font-family:"Tinos","Times New Roman",serif}

/* header */
.topbar{left:740px;top:0;width:460px;height:35px;background:var(--grey-bar)}
.call{left:790px;top:9px;font-size:13px;color:var(--ink)}
.round{border-radius:50%;background:var(--navy);width:26px;height:26px}
.brand{left:172px;top:76px;font-family:"Tinos",serif;font-weight:700;font-size:20px;color:var(--navy);letter-spacing:.5px}
.brand-mark{left:172px;top:22px;width:44px;height:44px;background:var(--navy)}
.search{left:787px;top:57px;width:250px;height:38px;border:1px solid #cfd3d8;background:var(--white)}
.search span{position:absolute;left:10px;top:10px;font-size:12px;color:#999;font-family:"Tinos",serif}
.search-btn{left:1000px;top:57px;width:37px;height:38px;background:var(--navy)}
.nav{left:0;top:114px;width:1200px;height:45px;background:linear-gradient(#2a5f9b,#14406f)}
.nav a{position:absolute;top:13px;font-family:"Tinos",serif;font-size:14px;color:var(--white);text-decoration:none}

/* hero */
.hero{left:0;top:159px;width:1200px;height:501px;background:linear-gradient(180deg,#4f86c6 0%,#7aa7d6 30%,#8c7f6a 65%,#4a4038 100%)}
.hero-caption{left:0;top:574px;width:1200px;height:86px;background:rgba(20,25,30,.55);text-align:center}
.hero-caption h2{font-family:"Raleway",sans-serif;font-weight:600;font-size:24px;color:var(--sky);margin-top:10px}
.hero-caption p{font-family:"Raleway",sans-serif;font-size:26px;color:var(--white);margin-top:2px}
.slide-arrow{top:385px;width:36px;height:30px;background:#2b2b2b}

/* about */
.section-title{left:0;width:1200px;text-align:center;font-family:"Tinos",serif;font-size:31px;color:var(--ink)}
.section-title em{font-style:normal;color:var(--blue)}
.rule{left:500px;width:200px;height:1px;background:#bbb}
.rule::after{content:"";position:absolute;left:84px;top:-1px;width:32px;height:3px;background:var(--navy)}
.about-text{left:170px;top:778px;width:860px;text-align:center;font-size:10.5px;line-height:17px;color:var(--muted)}

/* services */
.hex{width:216px;height:242px;clip-path:polygon(50% 0,100% 25%,100% 75%,50% 100%,0 75%,0 25%);background:#d8d8d8}
.hex-inner{position:absolute;left:8px;top:9px;width:200px;height:224px;clip-path:polygon(50% 0,100% 25%,100% 75%,50% 100%,0 75%,0 25%)}
.hex-label{position:absolute;left:0;width:200px;top:150px;text-align:center;font-family:"Tinos",serif;font-size:16px;color:var(--white)}
.hex-lead .hex-inner{background:var(--navy)}
.hex-lead .hex-label{top:70px;font-size:38px;line-height:42px}

/* why */
.why{left:0;top:1407px;width:1200px;height:434px;background:var(--navy)}
.why h2{color:var(--white)}
.point h3{font-family:"Tinos",serif;font-weight:700;font-size:16px;color:var(--white);line-height:18px}
.point p{font-size:11.5px;line-height:16px;color:#dce6f2;margin-top:2px}
.point.right-align{text-align:right}
.icon{width:72px;height:72px;border-radius:50%;background:var(--white);display:flex;align-items:center;justify-content:center}

/* testimonials */
.quote{left:242px;top:1982px;width:716px;text-align:center;font-style:italic;font-size:14px;line-height:26px;color:#333}
.who{left:0;width:1200px;text-align:center}

/* newsletter */
.newsletter{left:0;top:2199px;width:1200px;height:66px;background:linear-gradient(#4a4a4a,#1f1f1f)}
.news-title{left:258px;top:2214px;font-family:"Tinos",serif;font-size:27px;color:var(--white)}
.news-input{left:660px;top:2215px;width:258px;height:32px;background:var(--white);font-size:11px;color:#444;padding:9px 8px}
.news-btn{left:918px;top:2215px;width:122px;height:32px;background:var(--blue);color:var(--white);font-size:13px;text-align:center;padding-top:7px}

/* footer */
.footer{left:0;top:2265px;width:1200px;height:284px;background:var(--footer)}
.foot-h{top:2310px;font-family:"Tinos",serif;font-size:17px;color:var(--white)}
.foot-links{left:165px;top:2350px;list-style:none;font-family:"Tinos",serif;font-size:13px;line-height:22px;color:var(--white)}
.foot-links li::before{content:"› ";}
.contact{font-family:"Tinos",serif;font-size:13px;color:var(--white);line-height:19px}
.field{left:607px;width:208px;background:var(--white);font-size:11px;color:#444;padding:7px 7px}
.submit{left:607px;top:2497px;width:105px;height:32px;background:#111;color:var(--white);font-family:"Tinos",serif;font-size:15px;padding:6px 0 0 12px}
.vline{top:2310px;width:1px;height:205px;background:rgba(255,255,255,.25)}
.copyright{left:0;top:2549px;width:1200px;height:45px;background:var(--dark);text-align:center;font-family:"Tinos",serif;font-size:13px;color:#ddd;padding-top:14px}
</style>
</head>
<body>

<!-- header -->
<div class="abs topbar"></div>
<div class="abs round" style="left:754px;top:5px"></div>
<svg class="abs" style="left:760px;top:11px" width="14" height="14" viewBox="0 0 24 24"><path fill="#fff" d="M6.6 10.8a15 15 0 0 0 6.6 6.6l2.2-2.2c.3-.3.7-.4 1-.2 1.1.4 2.3.6 3.6.6.6 0 1 .4 1 1V20c0 .6-.4 1-1 1A17 17 0 0 1 3 4c0-.6.4-1 1-1h3.5c.6 0 1 .4 1 1 0 1.3.2 2.5.6 3.6.1.3 0 .7-.2 1z"/></svg>
<div class="abs call">Call : 123-456-7890</div>
<div class="abs round" style="left:917px;top:4px"></div>
<div class="abs round" style="left:948px;top:4px"></div>
<div class="abs round" style="left:978px;top:4px"></div>
<div class="abs round" style="left:1009px;top:4px"></div>

<div class="abs brand-mark"></div>
<div class="abs brand">PETER LASKO-WREN FINANCE</div>

<div class="abs search"><span>Search here...</span></div>
<div class="abs search-btn"></div>
<svg class="abs" style="left:1010px;top:67px" width="18" height="18" viewBox="0 0 24 24"><circle cx="10" cy="10" r="6.5" fill="none" stroke="#fff" stroke-width="2.6"/><path d="M15 15l6 6" stroke="#fff" stroke-width="2.8" stroke-linecap="round"/></svg>

<nav class="abs nav">
  <a style="left:175px">Home</a>
  <a style="left:239px">Equipment Finance</a>
  <a style="left:381px">Business Finance</a>
  <a style="left:512px">Commercial Finance</a>
  <a style="left:666px">Construction Finance</a>
  <a style="left:821px">Bridging Finance</a>
  <a style="left:956px">Contact Us</a>
</nav>

<!-- hero -->
<div class="abs hero" role="img" aria-label="Photo looking up at glass towers under construction with two workers in white hard hats"></div>
<div class="abs slide-arrow" style="left:0"></div>
<div class="abs slide-arrow" style="left:1164px"></div>
<svg class="abs" style="left:12px;top:393px" width="12" height="14"><path d="M9 2L3 7l6 5" fill="none" stroke="#fff" stroke-width="2"/></svg>
<svg class="abs" style="left:1176px;top:393px" width="12" height="14"><path d="M3 2l6 5-6 5" fill="none" stroke="#fff" stroke-width="2"/></svg>
<div class="abs hero-caption">
  <h2>Construction Finance</h2>
  <p>Focus on What you do Best, While We take care of your finances</p>
</div>

<!-- about -->
<h2 class="abs section-title" style="top:690px">About Peter Lasko <em>- Wren Finance</em></h2>
<div class="abs rule" style="top:745px"></div>
<p class="abs about-text">Lorem ipsum dolor sit amet, consectetuer adipiscing elit, sed diam nonummy nibh euismod tincidunt ut laoreet dolore magna aliquam erat volutpat. Ut wisi enim ad minim veniam, quis nostrud exerci tation ullamcorper suscipit lobortis nisl ut aliquip ex ea commodo consequat. Duis autem vel eum iriure dolor in hendrerit in vulputate velit esse molestie consequat, vel illum dolore eu feugiat nulla facilisis at vero eros et accumsan iusto odio dignissim qui blandit praesent luptatum zzril delenit augue duis dolore te feugait nulla facilisi. Ut wisi enim ad minim veniam, quis nostrud exerci tation ullamcorper suscipit lobortis nisl ut aliquip ex ea commodo consequat. Duis autem vel eum iriure dolor in hendrerit.</p>

<!-- services -->
<div class="abs hex" style="left:269px;top:916px"><div class="hex-inner" role="img" aria-label="Excavator on a dusk construction site" style="background:linear-gradient(#3d5a80,#6d6a5e)"><div class="hex-label">Equipment Finance</div></div></div>
<div class="abs hex hex-lead" style="left:494px;top:916px"><div class="hex-inner"><div class="hex-label">Our<br>Services</div></div></div>
<div class="abs hex" style="left:718px;top:916px"><div class="hex-inner" role="img" aria-label="Hands reviewing financial charts on paper" style="background:linear-gradient(#b9c9dc,#5d7fa5)"><div class="hex-label">Business Finance</div></div></div>
<div class="abs hex" style="left:155px;top:1120px"><div class="hex-inner" role="img" aria-label="Business handshake" style="background:linear-gradient(#9bb3cc,#2d4e75)"><div class="hex-label">Commercial Finance</div></div></div>
<div class="abs hex" style="left:380px;top:1120px"><div class="hex-inner" role="img" aria-label="Tall tower under construction with cranes" style="background:linear-gradient(#9fb8d6,#6b5a4c)"><div class="hex-label">Construction Finance</div></div></div>
<div class="abs hex" style="left:604px;top:1120px"><div class="hex-inner" role="img" aria-label="Stones arranged in an arch by the sea" style="background:linear-gradient(#c7ccd2,#6f7886)"><div class="hex-label">Bridging Finance</div></div></div>
<div class="abs hex" style="left:827px;top:1120px"><div class="hex-inner" role="img" aria-label="People signing documents at a desk" style="background:linear-gradient(#e4e2dd,#8c8a86)"><div class="hex-label">Others</div></div></div>

<!-- why choose us -->
<section class="abs why"></section>
<h2 class="abs section-title" style="top:1448px;color:#fff;font-size:28px">Why Choose Us</h2>
<div class="abs rule" style="top:1484px;background:rgba(255,255,255,.4)"></div>

<svg class="abs" style="left:0;top:1407px" width="1200" height="434">
  <g stroke="#cfdcea" stroke-width="2" stroke-dasharray="2 4" fill="none">
    <path d="M536 242 L558 302"/><path d="M662 242 L641 302"/>
    <path d="M450 292 L496 338"/><path d="M744 292 L703 338"/>
    <path d="M412 373 L445 382"/><path d="M786 373 L755 382"/>
  </g>
  <path d="M430 434 A170 170 0 0 1 770 434Z" fill="#fff" stroke="#2f7fd0" stroke-width="6"/>
  <g fill="#fff" stroke="#1b4d86" stroke-width="2">
    <circle cx="558" cy="304" r="6"/><circle cx="641" cy="304" r="6"/>
    <circle cx="496" cy="339" r="6"/><circle cx="703" cy="339" r="6"/>
    <circle cx="445" cy="383" r="6"/><circle cx="755" cy="383" r="6"/>
  </g>
  <text x="600" y="400" text-anchor="middle" font-family="Tinos, serif" font-size="22" font-weight="700" fill="#1b4d86">Peter Lasko-Wren</text>
</svg>

<div class="abs icon" style="left:500px;top:1575px"><svg width="34" height="34" viewBox="0 0 24 24"><path fill="#1b4d86" d="M6.6 10.8a15 15 0 0 0 6.6 6.6l2.2-2.2c.3-.3.7-.4 1-.2 1.1.4 2.3.6 3.6.6.6 0 1 .4 1 1V20c0 .6-.4 1-1 1A17 17 0 0 1 3 4c0-.6.4-1 1-1h3.5c.6 0 1 .4 1 1 0 1.3.2 2.5.6 3.6.1.3 0 .7-.2 1z"/></svg></div>
<div class="abs icon" style="left:626px;top:1575px"><svg width="34" height="34" viewBox="0 0 24 24"><circle cx="10" cy="8" r="4.5" fill="#1b4d86"/><path d="M2 22c0-5 3.6-8 8-8s8 3 8 8z" fill="#1b4d86"/><circle cx="19" cy="6" r="3.5" fill="none" stroke="#1b4d86" stroke-width="1.6"/></svg></div>
<div class="abs icon" style="left:393px;top:1632px"><svg width="34" height="34" viewBox="0 0 24 24"><circle cx="9" cy="14" r="5" fill="none" stroke="#1b4d86" stroke-width="3.5" stroke-dasharray="2.6 1.3"/><circle cx="17.5" cy="6.5" r="3.2" fill="none" stroke="#1b4d86" stroke-width="2.4" stroke-dasharray="1.8 1"/></svg></div>
<div class="abs icon" style="left:728px;top:1632px"><svg width="34" height="34" viewBox="0 0 24 24"><rect x="2" y="4" width="16" height="15" rx="1.5" fill="none" stroke="#1b4d86" stroke-width="2"/><path d="M2 8h16M6 2v4M14 2v4" stroke="#1b4d86" stroke-width="2"/><circle cx="18" cy="18" r="5" fill="#fff" stroke="#1b4d86" stroke-width="2"/><path d="M18 15.5V18h2" stroke="#1b4d86" stroke-width="1.6" fill="none"/></svg></div>
<div class="abs icon" style="left:344px;top:1727px"><svg width="34" height="34" viewBox="0 0 24 24"><path d="M12 5a6 6 0 0 0-3.5 10.9V18h7v-2.1A6 6 0 0 0 12 5z" fill="#1b4d86"/><rect x="9" y="19" width="6" height="2" fill="#1b4d86"/><path d="M12 0v3M3 6l2 1.5M21 6l-2 1.5M1 13h2.5M20.5 13H23" stroke="#1b4d86" stroke-width="1.6"/></svg></div>
<div class="abs icon" style="left:785px;top:1727px"><svg width="34" height="34" viewBox="0 0 24 24"><circle cx="7" cy="7" r="3.5" fill="#1b4d86"/><circle cx="17" cy="7" r="3.5" fill="#1b4d86"/><path d="M1 18c0-4 2.7-6 6-6s6 2 6 6zM11 18c0-4 2.7-6 6-6s6 2 6 6z" fill="#1b4d86"/></svg></div>

<div class="abs point right-align" style="left:179px;top:1530px;width:300px"><h3>Unbiased Recommendations</h3><p>Lorem ipsum dolor sit mork<br>[+]...adipiscing sed diam</p></div>
<div class="abs point right-align" style="left:174px;top:1614px;width:200px"><h3>Unparalleled<br>Service</h3><p>Lorem ipsum dolor sit mork<br>[+]...adipiscing sed diam</p></div>
<div class="abs point right-align" style="left:122px;top:1742px;width:200px"><h3>Superior Advice</h3><p>Lorem ipsum dolor sit mork<br>[+]...adipiscing sed diam</p></div>
<div class="abs point" style="left:721px;top:1530px;width:260px"><h3>Expert Guidance</h3><p>Lorem ipsum dolor sit mork<br>adipiscing sed diam...[+]</p></div>
<div class="abs point" style="left:825px;top:1628px;width:220px"><h3>Considerable Time<br>For You</h3><p>Lorem ipsum dolor sit mork<br>adipiscing sed diam...[+]</p></div>
<div class="abs point" style="left:878px;top:1727px;width:220px"><h3>Deep Legal Industry<br>Relationships</h3><p>Lorem ipsum dolor sit mork<br>adipiscing sed diam...[+]</p></div>

<!-- testimonials -->
<h2 class="abs section-title" style="top:1908px;font-size:28px">Clients <em>Testimonials</em></h2>
<div class="abs rule" style="top:1950px"></div>
<svg class="abs" style="left:135px;top:2005px" width="26" height="50"><path d="M22 2L4 25l18 23" fill="none" stroke="#9aa5b1" stroke-width="1.5"/></svg>
<svg class="abs" style="left:1039px;top:2005px" width="26" height="50"><path d="M4 2l18 23L4 48" fill="none" stroke="#9aa5b1" stroke-width="1.5"/></svg>
<div class="abs serif" style="left:192px;top:1968px;font-size:44px;color:#bbb">“</div>
<div class="abs serif" style="left:770px;top:2032px;font-size:44px;color:#bbb">”</div>
<p class="abs quote">Lorem ipsum dolor sit amet, consectetuer adipiscing elit, sed diam nonummy nibh euismod tinciduntol ut laoreet dolore magna aliquam erat volutpat. Ut wisi enim ad minim veniam, quis nostrud exercimori mormkle tation ullamcorper suscipit lobortis nisl ut aliquip ex ea commodo consequat.</p>
<div class="abs who" style="top:2078px;font-size:14px;font-weight:600;color:var(--blue)">Marla T.</div>
<div class="abs who" style="top:2101px;font-size:13px;color:#333">Lindale, CA</div>
<svg class="abs" style="left:570px;top:2141px" width="60" height="12"><circle cx="6" cy="6" r="4" fill="#1c68b5"/><circle cx="21" cy="6" r="4" fill="#999"/><circle cx="36" cy="6" r="4" fill="#999"/><circle cx="51" cy="6" r="4" fill="#999"/></svg>

<!-- newsletter -->
<div class="abs newsletter"></div>
<svg class="abs" style="left:162px;top:2208px" width="80" height="46" viewBox="0 0 80 46"><path d="M2 14h14M6 22h12M0 30h14" stroke="#fff" stroke-width="2.4"/><rect x="22" y="6" width="50" height="34" fill="none" stroke="#fff" stroke-width="3" transform="rotate(-8 47 23)"/><path d="M24 10l24 16 22-20" fill="none" stroke="#fff" stroke-width="3" transform="rotate(-8 47 23)"/></svg>
<div class="abs news-title">Subscribe Our Newsletter</div>
<svg class="abs" style="left:570px;top:2218px" width="72" height="28"><path d="M2 20c20 6 42 4 64-12" fill="none" stroke="#fff" stroke-width="1.8"/><path d="M56 6l10 2-4 9" fill="none" stroke="#fff" stroke-width="1.8"/></svg>
<div class="abs news-input">Enter Your Email Address</div>
<div class="abs news-btn">SUBSCRIBE</div>

<!-- footer -->
<footer class="abs footer"></footer>
<div class="abs" role="img" aria-label="Faint world map behind contact details" style="left:361px;top:2380px;width:230px;height:130px;background:rgba(255,255,255,.06);border-radius:40px"></div>
<div class="abs vline" style="left:335px"></div>
<div class="abs vline" style="left:583px"></div>
<div class="abs vline" style="left:830px"></div>

<div class="abs foot-h" style="left:165px">Quick Links</div>
<ul class="abs foot-links">
  <li>Home</li><li>Equipment Finance</li><li>Business Finance</li><li>Commercial Finance</li><li>Construction Finance</li><li>Bridging Finance</li><li>Contact Us</li>
</ul>

<div class="abs foot-h" style="left:361px">Contact Details</div>
<svg class="abs" style="left:357px;top:2354px" width="16" height="16" viewBox="0 0 24 24"><circle cx="12" cy="12" r="12" fill="#fff"/><path d="M12 5a4.5 4.5 0 0 0-4.5 4.5C7.5 13 12 19 12 19s4.5-6 4.5-9.5A4.5 4.5 0 0 0 12 5z" fill="#0d4f94"/></svg>
<div class="abs contact" style="left:382px;top:2352px">Peter Lasko-Wren Finance<br>Street Name City Name<br>State Zipcode</div>
<svg class="abs" style="left:357px;top:2421px" width="16" height="16" viewBox="0 0 24 24"><circle cx="12" cy="12" r="12" fill="#fff"/><path fill="#0d4f94" d="M9 10.5a9 9 0 0 0 4.5 4.5l1.5-1.5 2.5 1v3c-6 0-11-5-11-11h3l1 2.5z"/></svg>
<div class="abs contact" style="left:382px;top:2420px">123-456-7890</div>
<svg class="abs" style="left:357px;top:2457px" width="16" height="16" viewBox="0 0 24 24"><circle cx="12" cy="12" r="12" fill="#fff"/><rect x="6" y="8" width="12" height="9" fill="#0d4f94"/></svg>
<div class="abs contact" style="left:382px;top:2456px">123-456-7890</div>
<svg class="abs" style="left:357px;top:2493px" width="16" height="16" viewBox="0 0 24 24"><circle cx="12" cy="12" r="12" fill="#fff"/><rect x="6" y="8" width="12" height="8" fill="#0d4f94"/><path d="M6 8l6 5 6-5" stroke="#fff" fill="none" stroke-width="1.2"/></svg>
<div class="abs contact" style="left:382px;top:2492px">inquiry@laskowrenfin.com</div>

<div class="abs foot-h" style="left:609px">Quick Inquiry</div>
<div class="abs field" style="top:2352px;height:33px">Name</div>
<div class="abs field" style="top:2390px;height:30px">Email</div>
<div class="abs field" style="top:2428px;height:62px">Message</div>
<div class="abs submit">Submit &nbsp;→</div>

<div class="abs foot-h" style="left:851px">Follow Us</div>
<div class="abs" style="left:860px;top:2353px;width:28px;height:28px;border-radius:50%;background:#fff"></div>
<div class="abs" style="left:893px;top:2353px;width:28px;height:28px;border-radius:50%;background:#fff"></div>
<div class="abs" style="left:926px;top:2353px;width:28px;height:28px;border-radius:50%;background:#fff"></div>
<div class="abs" style="left:959px;top:2353px;width:28px;height:28px;border-radius:50%;background:#fff"></div>
<div class="abs serif" style="left:858px;top:2440px;font-size:18px;font-weight:700;color:rgba(255,255,255,.18)">Peter Lasko-Wren</div>

<div class="abs copyright">Copyright © 2017 Peter Lasko-Wren Finance. All Rights Reserved.</div>

</body>
</html>
```